Insurance Firm needs Stationary and Corporate Identity

We have a logo (provided) - we need a business card, letterhead, booklet cover, Benefit & Travel card design, and brand guide.
LRC (Larkmoor Relief Cooperative) is a National (Canadian) family-run benefits firm. We've been providing alternative benefit models to small and medium sized businesses for almost 25 years! Our goal is to create long-lasting customer relationships by partnering with our clients to become their dedicated benefits division instead of just selling a product to them.

Benefit & Travel Cards: We provide the benefit card to employees to allow them to pay for drugs at their pharmacy and dental services electronically.
The travel card is for medical emergencies while travelling outside of Canada.

Brand Guide: Once the stationary is complete, the brand guide will allow us to streamline the use of our logo's and fonts for internal and external use. We will expect that this will be a paid project for our design winner after the contest closes and we will negotiate the pricetag for this at that time.

Target Market(s)

Business Owners, Entrepreneurs, HR Professionals

Industry/Entity Type

Insurance Agency

Font styles to use
Sans Serif

Requirements
Must have
• business card, letterhead, health card, travel card, booklet cover (some current samples provided)

```html
<!DOCTYPE html>
<html lang="en">
<head>
<meta charset="utf-8">
<title>LRC Presentation Folder</title>
<link rel="stylesheet" href="https://fonts.googleapis.com/css2?family=Montserrat:wght@500&display=swap">
<style>
  :root {
    --navy: #263852;
    --navy-deep: #22334b;
    --red: #ec1f00;
    --red-line: #f2585a;
    --grey: #95979a;
    --page: #ffffff;
  }
  html, body {
    margin: 0;
    padding: 0;
    width: 1200px;
    height: 1200px;
    overflow: hidden;
    background: var(--page);
  }
  .canvas {
    position: relative;
    width: 1200px;
    height: 1200px;
  }
  .folder-cover {
    position: absolute;
    left: 150px;
    top: 210px;
    width: 520px;
    height: 780px;
    background: var(--navy);
    overflow: hidden;
  }
  .cover-pattern {
    position: absolute;
    inset: 0;
    background: radial-gradient(circle at 50% 55%, var(--navy) 0%, var(--navy-deep) 100%);
    opacity: 0.6;
  }
  .brand-name {
    position: absolute;
    top: 38px;
    right: 36px;
    margin: 0;
    font-family: "Montserrat", sans-serif;
    font-weight: 500;
    font-size: 78px;
    line-height: 1;
    letter-spacing: 2px;
    color: var(--grey);
  }
  .corner-stripes {
    position: absolute;
    right: 0;
    bottom: 0;
    width: 170px;
    height: 170px;
  }
  .folder-inside {
    position: absolute;
    left: 700px;
    top: 210px;
    width: 360px;
    height: 780px;
    background: var(--navy);
    overflow: hidden;
  }
  .inside-pocket {
    position: absolute;
    left: 0;
    bottom: 0;
    width: 360px;
    height: 460px;
  }
</style>
</head>
<body>
<main class="canvas">
  <section class="folder-cover" aria-label="Folder front cover">
    <div class="cover-pattern" role="img" aria-label="Faint tone-on-tone circle pattern across the navy cover"></div>
    <h1 class="brand-name">LRC</h1>
    <svg class="corner-stripes" viewBox="0 0 170 170" aria-hidden="true">
      <g stroke="var(--red-line)" stroke-width="4">
        <line x1="20" y1="170" x2="170" y2="20"/>
        <line x1="48" y1="170" x2="170" y2="48"/>
        <line x1="76" y1="170" x2="170" y2="76"/>
        <line x1="104" y1="170" x2="170" y2="104"/>
      </g>
    </svg>
  </section>

  <section class="folder-inside" aria-label="Folder inside panel with pocket">
    <svg class="inside-pocket" viewBox="0 0 360 460" aria-hidden="true">
      <path d="M0 30 Q180 -30 360 30 L360 460 L0 460 Z" fill="var(--red)"/>
    </svg>
  </section>
</main>
</body>
</html>
```